Natural Skincare brand needs new labels!

We are a natural and organic skin care brand based in the united states. We are looking for unique product label designs that will help our brand stand out. We want the labels to look elegant and natural, but also incorporate some color. We want a design aspect like a line drawing on the labels, see examples. Please refer to our website to see our current labels and to get more of a feel of who we are. Our logo is included. We are looking for 5 labels for 5 different Products.
1. Body butter: 1.5"x9" rectangle wrap around 12oz jar with black lid
2. Eczema Salve: 1.5" circle silver metal tin
3. Glow Serum: 1.5"x3" rectangle Blue Dropper Bottle with black top
4. Mineral Mist: 1.5"x3" clear glass sprayer bottle (want clear label)
website: www.venalubotanics.com
Instagram: @venalubotanics

```html
<!DOCTYPE html>
<html lang="en">
<head>
<meta charset="utf-8">
<title>Venalu Skin — Glow Serum Label</title>
<link rel="stylesheet" href="https://fonts.googleapis.com/css2?family=League+Spartan:wght@500&family=Montserrat:wght@400;500;700&display=swap">
<style>
  :root {
    --page: #ffffff;
    --label-ground: #f5f5f5;
    --lavender: #a08ac6;
    --coral: #f2877a;
    --charcoal: #3d3d3d;
    --ink: #2e2e2e;
    --dot: #9a9a9a;
    --sketch-tone: #e4e4e4;
  }
  * { margin: 0; padding: 0; box-sizing: border-box; }
  html, body {
    width: 756px;
    height: 1200px;
    overflow: hidden;
    background: var(--page);
  }
  .canvas {
    position: relative;
    width: 756px;
    height: 1200px;
    background: var(--page);
  }
  .label {
    position: absolute;
    left: 108px;
    top: 60px;
    width: 495px;
    height: 990px;
    transform: scale(1.0909);
    transform-origin: 0 0;
    background: var(--label-ground);
    overflow: hidden;
    font-family: "Montserrat", Arial, sans-serif;
    color: var(--ink);
  }
  .scallop-band {
    position: absolute;
    left: 0;
    top: 0;
    width: 495px;
    height: 64px;
  }
  .brand {
    position: absolute;
    left: 0;
    top: 180px;
    width: 495px;
    display: flex;
    align-items: center;
    justify-content: center;
    gap: 14px;
  }
  .brand-dot {
    width: 44px;
    height: 44px;
    border-radius: 50%;
    background: var(--coral);
    flex: none;
  }
  .brand-name {
    font-family: "Montserrat", Arial, sans-serif;
    font-weight: 500;
    font-size: 54px;
    letter-spacing: 1px;
    color: var(--coral);
    line-height: 1;
  }
  .product-title {
    position: absolute;
    left: 0;
    top: 418px;
    width: 495px;
    text-align: center;
    font-family: "League Spartan", "Montserrat", sans-serif;
    font-weight: 500;
    line-height: 0.82;
  }
  .product-title .line-glow {
    display: block;
    font-size: 96px;
    color: var(--charcoal);
    letter-spacing: -1px;
  }
  .product-title .line-serum {
    display: block;
    font-size: 96px;
    color: var(--coral);
    letter-spacing: -1px;
  }
  .dot-rule {
    position: absolute;
    left: 94px;
    width: 316px;
    height: 3px;
    background-image: radial-gradient(circle, var(--dot) 1px, transparent 1.3px);
    background-size: 21px 3px;
    background-repeat: repeat-x;
  }
  .dot-rule--upper { top: 621px; }
  .dot-rule--lower { top: 727px; }
  .benefits {
    position: absolute;
    left: 0;
    top: 648px;
    width: 495px;
    text-align: center;
    font-size: 21px;
    line-height: 28px;
    color: var(--ink);
  }
  .ingredients {
    position: absolute;
    left: 94px;
    top: 766px;
    width: 232px;
    font-size: 16.5px;
    line-height: 21.4px;
    color: var(--ink);
  }
  .ingredients strong { font-weight: 700; }
  .botanical-sketch {
    position: absolute;
    left: 334px;
    top: 728px;
    width: 161px;
    height: 242px;
    background: linear-gradient(160deg, var(--label-ground) 0%, var(--sketch-tone) 100%);
  }
  .volume-tab {
    position: absolute;
    left: 339px;
    top: 907px;
    width: 72px;
    height: 75px;
    border-radius: 30px 30px 0 0;
    background: var(--coral);
    color: #ffffff;
    font-family: "League Spartan", "Montserrat", sans-serif;
    font-size: 22px;
    text-align: center;
    padding-top: 24px;
  }
  .volume-tab sup { font-size: 12px; }
  .base-band {
    position: absolute;
    left: 0;
    bottom: 0;
    width: 495px;
    height: 19px;
    background: var(--coral);
  }
</style>
</head>
<body>
<main class="canvas">
  <section class="label">
    <svg class="scallop-band" viewBox="0 0 495 64" aria-hidden="true">
      <path fill="var(--lavender)" d="M0 0 H495 V50 q-8.84 14 -17.68 0 t-17.68 0 t-17.68 0 t-17.68 0 t-17.68 0 t-17.68 0 t-17.68 0 t-17.68 0 t-17.68 0 t-17.68 0 t-17.68 0 t-17.68 0 t-17.68 0 t-17.68 0 t-17.68 0 t-17.68 0 t-17.68 0 t-17.68 0 t-17.68 0 t-17.68 0 t-17.68 0 t-17.68 0 t-17.68 0 t-17.68 0 t-17.68 0 t-17.68 0 t-17.68 0 t-17.68 0 Z"/>
    </svg>

    <div class="brand">
      <span class="brand-dot"></span>
      <span class="brand-name">Venalu Skin</span>
    </div>

    <h1 class="product-title">
      <span class="line-glow">GLOW</span>
      <span class="line-serum">SERUM</span>
    </h1>

    <div class="dot-rule dot-rule--upper"></div>
    <p class="benefits">Mouisturizing+Nourishing<br>Sensitive+Dry Skin</p>
    <div class="dot-rule dot-rule--lower"></div>

    <p class="ingredients"><strong>Ingredients</strong>: safflower oil^, sesame oil^, manjistha powder^, rose petals^, turmeric^, carrot seed oil^, sandalwood essential oil, ylang ylang essential oil</p>

    <div class="botanical-sketch" role="img" aria-label="Black line drawing of a flowering botanical stem with leaves"></div>

    <div class="volume-tab">12<sup>OZ</sup></div>
    <div class="base-band"></div>
  </section>
</main>
</body>
</html>
```